Bring me business with this creative business card

Design my new business card. I am looking for something different with an impact. People will take a look at this card & they will 1- see how different & creative I am, 2-understand what I do 3- Call me to meet me!

I make videos with a message, testimonials. I am dynamic, fun, creative & human. My new website is in construction but in the meantime you can check this old one: brightpath.ca & another one Ferncove.com & ferncove facebook page.
I make videos. sometimes with a cameraman, sometimes with my phone. As an ex Public Relations agent, the message is the most important thing for me. I want to make my clients shine! When they start with me they often remind me of a lamb, when I finish coaching them they are powerful like LIONS! That's why I need a powerful business card!

Target Market(s)

Entrepreneurs, solo entrepreneurs, small & medium companies & start ups. People i will meet while networking. People that need videos on their website & social Networks to get attention, to be visible. men & women. From 35 to 49 years old.
I am an ex Public relations agent. I used to send clients in traditional medias, now with videos they have more chances to be seen on google the new media. I do videos of the president, his team, his loyal clients saying how great the company is & expert videos like series so people can be seen for example every 1 st of every month with a short 2 minute video. Also with my 20 years in marketing & communications I can coach & give tips to anybody who needs it.
Target: anybody who would like my old website brightpath.ca & I also have another website but it will be off line soon: ferncove.com could give you ideas.

Industry/Entity Type

Communications

Contact Information for Business Card

I am in Montreal,So the business cards have to be the usual size like we have in Montreal: 9 cm x 5 cm
Details:My text: Martine Gaudreau Communication coach/Chief Lion. "Creating Videos as unique as you" off: 514-555-3047 cell: 514-555-6182. ferncove.com
martine@ferncove.com logo facebook, youtube, instagram

Colors
f37122

Requirements
Must have
• Dynamic, happy. Orange. Be creative in the look but NOT the shape of the card. Easy to read. Big enough to read.
Should not have
• No funny shapes: no round, no square, just the usual. I love creative but NOT on shape.

```html
<!DOCTYPE html>
<html lang="en">
<head>
<meta charset="utf-8">
<title>Ferncove Business Card</title>
<link rel="stylesheet" href="https://fonts.googleapis.com/css2?family=Cinzel:wght@600&family=Open+Sans:ital,wght@0,400;0,600;1,400&display=swap">
<style>
  :root {
    --backdrop: #b4b4b4;
    --rust: #b2481d;
    --orange: #e05a1e;
    --orange-deep: #d9531c;
    --gold: #ee9a1f;
    --amber: #f3a626;
    --paper: #f7f6f3;
    --ink: #2b2b2b;
    --cream: #f1e6dc;
  }
  * { margin: 0; padding: 0; box-sizing: border-box; }
  html, body { width: 1200px; height: 576px; overflow: hidden; }
  body { background: var(--backdrop); position: relative; font-family: "Open Sans", sans-serif; }

  .card { position: absolute; top: 138px; height: 293px; box-shadow: 0 2px 4px rgba(0,0,0,.35); overflow: hidden; }

  /* Front */
  .card-front { left: 81px; width: 485px; background: var(--rust); }
  .front-mark {
    position: absolute; left: 50%; top: 56px; width: 110px; height: 110px;
    margin-left: -55px; border-radius: 50%; background: var(--amber);
  }
  .front-name {
    position: absolute; left: 0; right: 0; top: 190px; text-align: center;
    font-family: "Open Sans", sans-serif; font-weight: 600; font-size: 32px;
    letter-spacing: 2px; color: var(--cream);
  }

  /* Back */
  .card-back { left: 602px; width: 481px; background: var(--paper); }
  .back-wave { position: absolute; left: 0; top: 0; }
  .brand-name {
    position: absolute; left: 30px; top: 26px;
    font-family: "Open Sans", sans-serif; font-weight: 600; font-size: 32px;
    letter-spacing: 1px; color: var(--orange-deep); line-height: 1;
  }
  .back-mark {
    position: absolute; left: 322px; top: 22px; width: 124px; height: 124px;
    border-radius: 50%; background: var(--amber);
  }
  .person { position: absolute; left: 30px; top: 116px; }
  .person-name {
    font-family: "Cinzel", serif; font-weight: 600; font-size: 24px;
    color: var(--orange-deep); letter-spacing: .5px; line-height: 1.1;
  }
  .person-role { font-style: italic; font-size: 11px; color: var(--ink); margin-top: 2px; }
  .contacts { position: absolute; left: 30px; top: 168px; list-style: none; }
  .contacts li {
    display: flex; align-items: center; gap: 10px; height: 18.5px;
    font-size: 12.5px; color: var(--ink);
  }
  .contacts svg { width: 12px; height: 12px; fill: var(--orange); }
  .slogan {
    position: absolute; right: 26px; top: 210px; text-align: right;
    font-style: italic; font-size: 12px; line-height: 1.35; color: #fff;
  }
  .social {
    position: absolute; right: 26px; top: 254px; display: flex; align-items: center; gap: 6px;
    font-size: 13px; color: #fff;
  }
  .social .dot { width: 11px; height: 11px; border-radius: 50%; background: #fff; }
</style>
</head>
<body>
  <section class="card card-front">
    <div class="front-mark"></div>
    <div class="front-name">FERNCOVE</div>
  </section>

  <section class="card card-back">
    <svg class="back-wave" width="481" height="293" viewBox="0 0 481 293">
      <path fill="var(--orange-deep)" d="M0,262 C110,300 220,268 300,228 C370,194 420,172 481,166 L481,293 L0,293 Z"/>
      <path fill="var(--gold)" d="M0,236 C120,262 220,240 300,200 C370,166 420,150 481,146 L481,156 C420,160 372,178 304,212 C226,252 120,270 0,250 Z"/>
      <path fill="var(--gold)" d="M40,250 C130,280 230,262 330,208 C250,258 140,276 40,250 Z"/>
    </svg>

    <div class="brand-name">FERNCOVE</div>
    <div class="back-mark"></div>

    <div class="person">
      <div class="person-name">MARTINE G.</div>
      <div class="person-role">Communication coach / Chief</div>
    </div>

    <ul class="contacts">
      <li><svg viewBox="0 0 24 24"><path d="M6.6 10.8a15.1 15.1 0 0 0 6.6 6.6l2.2-2.2c.3-.3.7-.4 1-.2 1.1.4 2.3.6 3.6.6.6 0 1 .4 1 1V20c0 .6-.4 1-1 1A17 17 0 0 1 3 4c0-.6.4-1 1-1h3.5c.6 0 1 .4 1 1 0 1.3.2 2.5.6 3.6.1.3 0 .7-.2 1z"/></svg>514-555-3047, 514-555-6182</li>
      <li><svg viewBox="0 0 24 24"><path d="M2 5h20v14H2z"/><path d="M3.5 6.5 12 13l8.5-6.5" stroke="#fff" stroke-width="1.6" fill="none"/></svg>martine@ferncove.com</li>
      <li><svg viewBox="0 0 24 24"><circle cx="12" cy="12" r="10"/><path d="M2 12h20M12 2c3 3 3 17 0 20M12 2c-3 3-3 17 0 20" stroke="#fff" stroke-width="1.4" fill="none"/></svg>www.ferncove.com</li>
    </ul>

    <div class="slogan">Creating Videos<br>as unique as you</div>
    <div class="social"><span class="dot"></span>/ferncove</div>
  </section>
</body>
</html>
```